Night Dresses business cards business requirers

We are a new company initiating Mexico operations. Our core business is Night woman dress (both formal and party dress) for rent. Gownvella is the name of the company. ITS Gownvella form by two word. The dress word and topia (Utopic) so the place Gownvella Means That You cant get the ideal, perfect and unique dress for your event. So we would like a modern, very creative, and attractive business card.

Industry/Entity Type

Womens Clothing

Contact Information for Business Card

Rounded Borders, two faces

Requirements
Must have
• Rounded borders, logo and slogan, modern, glam, attractive design
Should not have
• modern design classic or not

```html
<!DOCTYPE html>
<html lang="en">
<head>
<meta charset="utf-8">
<title>Gownvella Business Card</title>
<link rel="stylesheet" href="https://fonts.googleapis.com/css2?family=Arimo:wght@400;700&display=swap">
<style>
  :root {
    --backdrop: #2b2b2d;
    --orchid: #b25a90;
    --orchid-light: #d9a6c4;
    --paper: #f7f7f7;
    --ink: #333333;
    --ink-soft: #666666;
    --white: #ffffff;
  }
  * { box-sizing: border-box; margin: 0; padding: 0; }
  html, body { width: 1200px; height: 997px; overflow: hidden; }
  body {
    background: var(--backdrop);
    font-family: "Arimo", Arial, sans-serif;
    display: flex; flex-direction: column; align-items: center;
    gap: 44px; padding-top: 48px;
  }
  .card {
    width: 760px; height: 430px; border-radius: 26px;
    position: relative; overflow: hidden;
    box-shadow: 0 14px 30px rgba(0,0,0,.45);
  }
  /* Front face */
  .card-front { background: var(--orchid); display: flex; align-items: center; justify-content: center; }
  .front-mark { display: flex; align-items: center; gap: 24px; }
  .front-circle { width: 84px; height: 84px; border: 6px solid var(--white); border-radius: 50%; }
  .front-name { color: var(--white); font-weight: 700; font-size: 52px; }
  /* Back face */
  .card-back { background: var(--paper); }
  .brand { position: absolute; left: 48px; top: 50px; display: flex; align-items: center; gap: 16px; }
  .brand-circle { width: 52px; height: 52px; border: 3px solid var(--orchid); border-radius: 50%; }
  .brand-name { font-weight: 700; font-size: 32px; color: var(--ink); }
  .slogan { position: absolute; left: 116px; top: 110px; font-size: 14px; color: var(--ink-soft); }
  .person { position: absolute; left: 80px; top: 205px; }
  .person-name { color: var(--orchid); font-weight: 700; font-size: 20px; }
  .person-role { color: var(--ink); font-size: 15px; margin-top: 4px; padding-left: 54px; }
  .divider {
    position: absolute; left: 380px; top: 160px; width: 2px; height: 110px;
    background: linear-gradient(var(--paper), var(--orchid), var(--paper));
  }
  .contact { position: absolute; left: 420px; top: 170px; list-style: none; color: var(--ink); font-size: 16px; line-height: 1.25; }
  .contact li { display: flex; gap: 12px; margin-bottom: 10px; }
  .contact svg { flex: none; margin-top: 1px; }
  .band {
    position: absolute; left: 0; right: 0; bottom: 0; height: 96px;
    background: var(--orchid); display: flex; align-items: center; justify-content: center;
    color: var(--orchid-light); font-size: 18px; font-weight: 700; letter-spacing: 2px;
    padding-top: 14px;
  }
  .band-circle {
    position: absolute; left: 50%; top: -24px; margin-left: -24px;
    width: 48px; height: 48px; border-radius: 50%;
    background: var(--paper); border: 3px solid var(--orchid);
  }
</style>
</head>
<body>
  <section class="card card-front" aria-label="Card front">
    <div class="front-mark">
      <span class="front-circle"></span>
      <span class="front-name">Gownvella</span>
    </div>
  </section>

  <section class="card card-back" aria-label="Card back">
    <div class="brand">
      <span class="brand-circle"></span>
      <span class="brand-name">Gownvella</span>
    </div>
    <p class="slogan">Evening dresses to rent</p>

    <div class="person">
      <div class="person-name">MARISOL VEGA</div>
      <div class="person-role">Attorney</div>
    </div>

    <div class="divider"></div>

    <ul class="contact">
      <li>
        <svg width="20" height="20" viewBox="0 0 20 20" aria-hidden="true">
          <circle cx="10" cy="10" r="10" fill="var(--orchid)"/>
          <path d="M6 7.5c0-1 .8-1.5 4-1.5s4 .5 4 1.5v1h-2v-1h-4v1H6z M7 10h6l1 4H6z" fill="var(--white)"/>
        </svg>
        <span>424 555 0137</span>
      </li>
      <li>
        <svg width="20" height="20" viewBox="0 0 20 20" aria-hidden="true">
          <circle cx="10" cy="10" r="10" fill="var(--orchid)"/>
          <rect x="5" y="6.5" width="10" height="7" fill="var(--white)"/>
          <path d="M5 6.5l5 4 5-4" fill="none" stroke="var(--orchid)" stroke-width="1.2"/>
        </svg>
        <span>2140 Alameda blvd,<br>Verano City, CA 90417</span>
      </li>
    </ul>

    <div class="band">
      <span class="band-circle"></span>
      2140 Alameda blvd, Verano City, CA 90417
    </div>
  </section>
</body>
</html>
```